Powerpoint Design and Build

We need to create PowerPoint for program called Glimmerly Orbit. Glimmerly Orbit is an online system that helps association volunteers track their volunteer hours and the impact that are having with engineering outreach initiatives.

We have an established logo for the brand, which you will find under Files.

The following colors are used in the brand:

Blue/green: PMS 3262 C

Purple: PMS 525 C

Lime: PMS 381 C

Grey: PMS Cool Grey 11

Headline and body fonts should be restricted to a common sans serif such as arial or helvetica

For reference, The tagline "Make Every Hour Shine" is set in Gotham Book; match to this.

The identity needs to be locked up with the Coalition of Harbor Artisans logo in grey, which you'll find attached. See the file "Glimmerly_orbit_lock-up.psd" for reference, but please recreate as a vector element.

As an idea of Powerpoint created for a different Coalition of Harbor Artisans program, place see the Tessera Powerpoint. FOR Reference only

NOTE: please maximize the area for content and stick to a white background.

Final deliverables are:

Design for presentation title slide, section title slide and content slide, including styles for headlines, subheads, bullet points and straight copy. Also include slide numbers in footer.

To repeat, we expect separate art elements created in Illustrator, and a completed Powerpoint template with master slides.

Professional and Collegiate Women in Engineering

Engineering

• Design for presentation title slide, section title slide and content slide, including styles for headlines, subheads, bullet points and straight copy. Also include slide numbers in footer.

```html
<!DOCTYPE html>
<html lang="en">
<head>
<meta charset="utf-8">
<title>Glimmerly Orbit – Title Slide</title>
<link rel="stylesheet" href="https://fonts.googleapis.com/css2?family=Arimo:wght@400;700&family=Montserrat:wght@400&display=swap">
<style>
  :root {
    --ink-blue: #0a80c2;
    --body-grey: #9a9a9a;
    --top-band: #eeeeee;
    --top-rule: #c4c4c4;
    --footer-rule: #2a8ac4;
    --footer-tint: #d6eefa;
    --hex-grey: #dedede;
    --hex-pale: #e2f3fc;
    --hex-blue: #7dbfe0;
    --brand-teal: #3aa9b4;
    --brand-grey: #5f6163;
    --badge-grey: #8c8c8c;
    --white: #ffffff;
  }
  html, body {
    margin: 0;
    padding: 0;
    width: 1200px;
    height: 900px;
    overflow: hidden;
    background: var(--white);
  }
  .slide {
    position: relative;
    width: 1200px;
    height: 900px;
    overflow: hidden;
    background: var(--white);
    font-family: "Arimo", Arial, sans-serif;
  }
  .top-band {
    position: absolute;
    left: 0; top: 0;
    width: 1200px; height: 58px;
    background: var(--top-band);
    border-bottom: 3px solid var(--top-rule);
  }
  .art {
    position: absolute;
    left: 0; top: 0;
    width: 1200px; height: 900px;
  }
  .title-block {
    position: absolute;
    left: 631px;
    top: 342px;
  }
  .course-title {
    margin: 0 0 12px;
    font-weight: 400;
    font-size: 40px;
    line-height: 1.1;
    color: var(--ink-blue);
  }
  .course-intro {
    margin: 0;
    font-size: 27px;
    line-height: 41px;
    color: var(--body-grey);
  }
  .footer {
    position: absolute;
    left: 0; top: 802px;
    width: 1200px; height: 98px;
    border-top: 3px solid var(--footer-rule);
    background: linear-gradient(to right, var(--white) 0, var(--white) 772px, var(--footer-tint) 772px);
  }
  .brand {
    position: absolute;
    left: 12px; top: 16px;
  }
  .brand-name {
    display: flex;
    align-items: center;
    gap: 10px;
    font-size: 48px;
    line-height: 1;
    font-weight: 400;
    color: var(--brand-teal);
    white-space: nowrap;
  }
  .brand-mark {
    width: 44px; height: 44px;
    border-radius: 50%;
    background: var(--brand-teal);
    flex: none;
  }
  .brand-tagline {
    margin: 5px 0 0 64px;
    font-family: "Montserrat", Arial, sans-serif;
    font-size: 14px;
    color: var(--brand-grey);
    white-space: nowrap;
  }
  .lockup-rule {
    position: absolute;
    left: 479px; top: 20px;
    width: 2px; height: 52px;
    background: #b5b5b5;
  }
  .partner {
    position: absolute;
    left: 505px; top: 24px;
    display: flex;
    align-items: center;
    gap: 10px;
    color: var(--brand-grey);
    font-size: 20px;
    line-height: 22px;
    white-space: nowrap;
  }
  .partner-mark {
    width: 40px; height: 40px;
    border-radius: 50%;
    background: var(--brand-grey);
    flex: none;
  }
  .slide-number {
    position: absolute;
    left: 1082px; top: 16px;
    width: 113px; height: 66px;
  }
  .slide-number svg { display: block; }
  .slide-number span {
    position: absolute;
    left: 0; top: 0;
    width: 90px; height: 66px;
    line-height: 66px;
    text-align: center;
    color: var(--white);
    font-weight: 700;
    font-size: 25px;
  }
</style>
</head>
<body>
<main class="slide">
  <div class="top-band"></div>

  <svg class="art" viewBox="0 0 1200 900" xmlns="http://www.w3.org/2000/svg">
    <defs>
      <linearGradient id="backdropFade" x1="0" y1="0" x2="1" y2="0">
        <stop offset="0" stop-color="#d9ecf8" stop-opacity="0.9"/>
        <stop offset="0.6" stop-color="#e6f2fa" stop-opacity="0.6"/>
        <stop offset="1" stop-color="#ffffff" stop-opacity="0"/>
      </linearGradient>
      <linearGradient id="portraitTone" x1="0" y1="0" x2="1" y2="1">
        <stop offset="0" stop-color="#e8eef3"/>
        <stop offset="0.55" stop-color="#c9d6e0"/>
        <stop offset="1" stop-color="#a9bccb"/>
      </linearGradient>
      <filter id="frameShadow" x="-20%" y="-20%" width="140%" height="140%">
        <feDropShadow dx="0" dy="2" stdDeviation="4" flood-color="#000" flood-opacity="0.25"/>
      </filter>
    </defs>

    <rect class="backdrop-wash" x="0" y="61" width="800" height="741" fill="url(#backdropFade)" role="img" aria-label="Soft blue backdrop texture"/>

    <g class="hex-cluster-top">
      <polygon points="345,137 384,159.5 384,204.5 345,227 306,204.5 306,159.5" fill="var(--hex-grey)"/>
      <polygon points="431,131 470,153.5 470,198.5 431,221 392,198.5 392,153.5" fill="var(--hex-pale)"/>
      <polygon points="389,209 428,231.5 428,276.5 389,299 350,276.5 350,231.5" fill="var(--hex-blue)"/>
    </g>

    <g class="hex-cluster-bottom">
      <polygon points="110,537 149,559.5 149,604.5 110,627 71,604.5 71,559.5" fill="var(--hex-grey)"/>
      <polygon points="196,533 235,555.5 235,600.5 196,623 157,600.5 157,555.5" fill="var(--hex-pale)"/>
      <polygon points="155,610 194,632.5 194,677.5 155,700 116,677.5 116,632.5" fill="var(--hex-blue)"/>
    </g>

    <g class="portrait-frame" filter="url(#frameShadow)">
      <polygon points="291,290 401,354 401,483 291,547 181,483 181,354" fill="var(--white)"/>
      <polygon points="291,299 393,358.5 393,478.5 291,538 189,478.5 189,358.5" fill="url(#portraitTone)" role="img" aria-label="Portrait of a smiling professional in an office"/>
    </g>
  </svg>

  <section class="title-block">
    <h1 class="course-title">Course Title Here</h1>
    <p class="course-intro">Course introdetails here</p>
    <p class="course-intro">Course introdetails here</p>
  </section>

  <footer class="footer">
    <div class="brand">
      <div class="brand-name"><span class="brand-mark"></span>Glimmerly Orbit</div>
      <div class="brand-tagline">Make Every Hour Shine</div>
    </div>
    <div class="lockup-rule"></div>
    <div class="partner">
      <span class="partner-mark"></span>
      <span>Coalition of<br>Harbor Artisans</span>
    </div>
    <div class="slide-number">
      <svg width="113" height="66" viewBox="0 0 113 66" xmlns="http://www.w3.org/2000/svg">
        <polygon points="0,0 80,0 113,33 80,66 0,66" fill="var(--badge-grey)"/>
      </svg>
      <span>01</span>
    </div>
  </footer>
</main>
</body>
</html>
```